Anzeigengestaltung für einen einen ambulanten Pflegedienst
Zielgruppe
Insgesamt möchte ich gern drei Anzeigen für das Internet gestalten haben. Ich betreibe einen ambulanten Pflegedienst. Die erste Anzeige soll dazu dienen Kunden anzusprechen, die einen Unterstützungsbedarf und / oder einen Beratungsbedarf haben. Die zweite Anzeige soll dazu dienen neues Personal anzuwerben. Die dritte Anzeige soll speziell potenzielle Azubis ansprechen. Die Anzeigen sind gedacht für Chatterwall und Pixelora hauptsächlich. In den Druck sollte es schon 10cm x 8cm sein. Es wäre super wenn vielleicht auch eine Art Aufruf an ehrenamtliche Mitarbeiter erfolgt.
Aufgabenstellung
Die Anzeigen sollen den Stil der Homepage beibehalten. Freundlich, frisch und agil wirken. Alle sollten emotional ansprechend sein und gerade der für zukünftige Mitarbeiter sollte deutlich ein gutes Betriebsklima vermitteln. Als Datei habe ich einige Bilder, die bereits für die Homepage oder Flyer verwendet wurden hochgeladen. des Weiteren habe ich die einzelnen Seiten des Flyers hochgeladen.

```html
<!DOCTYPE html>
<html lang="de">
<head>
<meta charset="utf-8">
<title>Lindar Pflege – Wir sind für Sie da</title>
<link rel="stylesheet" href="https://fonts.googleapis.com/css2?family=Playfair+Display:wght@400&family=Quicksand:wght@600;700&family=Raleway:wght@600&display=swap">
<style>
  :root {
    --paper: #edefeb;
    --white: #ffffff;
    --teal: #4aafad;
    --green: #7bb03a;
    --grey: #5f5f5f;
    --tone-leaf: #56604c;
    --tone-stone: #8f8b84;
    --tone-cream: #ece6db;
    --tone-linen: #d6cbbb;
    --tone-taupe: #9a8670;
  }
  html, body {
    margin: 0;
    padding: 0;
    overflow: hidden;
  }
  .ad {
    position: relative;
    width: 1200px;
    height: 960px;
    background: var(--paper);
    overflow: hidden;
  }
  .hero {
    position: absolute;
    left: 0;
    top: 0;
    width: 1200px;
    height: 960px;
  }
  .brand-badge {
    position: absolute;
    left: 480px;
    top: 408px;
    width: 240px;
    height: 240px;
    border-radius: 50%;
    background: var(--white);
  }
  .brand-mark {
    position: absolute;
    left: 80px;
    top: 56px;
    width: 72px;
    height: 72px;
    border-radius: 50%;
    border: 4px solid var(--green);
  }
  .brand-name {
    position: absolute;
    left: 0;
    width: 240px;
    top: 150px;
    margin: 0;
    text-align: center;
    font-family: "Raleway", sans-serif;
    font-weight: 600;
    font-size: 25px;
    line-height: 32px;
    letter-spacing: 0.3px;
    color: var(--grey);
  }
  .tagline {
    position: absolute;
    left: 60px;
    top: 618px;
    margin: 0;
    font-family: "Playfair Display", serif;
    font-weight: 400;
    font-size: 35px;
    line-height: 48px;
    color: var(--grey);
  }
  .headline {
    position: absolute;
    left: 60px;
    top: 693px;
    margin: 0;
    font-family: "Quicksand", sans-serif;
    font-weight: 700;
    font-size: 45.5px;
    line-height: 59px;
    color: var(--teal);
    letter-spacing: 0.4px;
  }
  .headline .accent {
    color: var(--green);
  }
  .divider {
    position: absolute;
    left: 60px;
    top: 851px;
    width: 1080px;
    height: 2px;
    background: var(--green);
  }
  .contact {
    position: absolute;
    top: 862px;
    margin: 0;
    font-family: "Playfair Display", serif;
    font-weight: 400;
    font-size: 36px;
    line-height: 50px;
    color: var(--grey);
  }
  .contact-phone { left: 60px; }
  .contact-mail { right: 60px; }
</style>
</head>
<body>
<main class="ad">
  <svg class="hero" viewBox="0 0 1200 960">
    <defs>
      <linearGradient id="heroTone" x1="0" y1="0" x2="1" y2="0.15">
        <stop offset="0" stop-color="var(--tone-leaf)"/>
        <stop offset="0.2" stop-color="var(--tone-stone)"/>
        <stop offset="0.42" stop-color="var(--tone-cream)"/>
        <stop offset="0.62" stop-color="var(--tone-linen)"/>
        <stop offset="1" stop-color="var(--tone-taupe)"/>
      </linearGradient>
    </defs>
    <path role="img" aria-label="Foto: eine ältere Dame in heller Strickjacke und Perlenkette lächelt einer Pflegerin zu, die liebevoll ihre Hand hält"
          d="M0 0 H1200 V315 Q600 736 0 317 Z" fill="url(#heroTone)"/>
  </svg>

  <div class="brand-badge">
    <span class="brand-mark"></span>
    <p class="brand-name">LINDAR PFLEGE</p>
  </div>

  <p class="tagline">Wir sind für Sie da!</p>

  <h1 class="headline">Nehmen Sie Kontakt mit uns für<br><span class="accent">Unterstützungs-/Beratungsbedarf</span> auf.</h1>

  <div class="divider"></div>

  <p class="contact contact-phone">012345/67 89 00</p>
  <p class="contact contact-mail">lindar-pflege@postfeld.de</p>
</main>
</body>
</html>
```